Vell Tarnmoor - Brochure - Industrial Construction Services

We need a brochure design based on the power point presentation attached. Our business is named Vell Tarnmoor and is an industrial project services business concentrating on Construction Project Management, Technical Services, and Consulting. We want to communicate that "We offer our clients a
unique systematic approach to solving technical challenges." As you can see from our logo designs we like the colors blue and grey. We are after clean, but innovative design overall. We also seem to like design that have darker style backgrounds. We would like this brochure to be a bi-fold 8.5"x 5.5" size when closed if possible. If any files or graphics are needed in original format please request them. Thanks!

Target Market(s)

Large Oil & Gas, Power Generation, and Engineering Companies.

Industry/Entity Type

Engineering

Font styles to use
Serif

Requirements
Must have
• A strong-lasting first impression.

```html
<!DOCTYPE html>
<html lang="en">
<head>
<meta charset="utf-8">
<title>Vell Tarnmoor – Brochure</title>
<link rel="stylesheet" href="https://fonts.googleapis.com/css2?family=EB+Garamond:wght@400;500&display=swap">
<style>
  :root {
    --ink: #3a3a3a;
    --white: #ffffff;
    --blue-top: #1f6fb0;
    --blue-bottom: #14508a;
    --grey-top: #6f6f6f;
    --grey-bottom: #4e4e4e;
    --panel-light: #ebebeb;
    --red: #d9291e;
    --red-deep: #c8221a;
    --bullet: #2b5f7a;
    --photo-dark: #1b1d1f;
    --photo-mid: #4a5054;
    --sky-top: #1d3138;
    --sky-mid: #6f8d92;
    --sky-low: #c9d3cf;
  }
  * { margin: 0; padding: 0; box-sizing: border-box; }
  html, body { width: 1200px; height: 926px; overflow: hidden; background: #ffffff; }
  body { font-family: "EB Garamond", Georgia, serif; color: var(--ink); }

  .brochure { position: relative; width: 1200px; height: 926px; }
  .panel { position: absolute; }

  .founders-photo {
    left: 0; top: 0; width: 600px; height: 428px;
    background: radial-gradient(ellipse at 45% 30%, var(--photo-mid) 0%, #2c3033 55%, var(--photo-dark) 100%);
  }
  .about-heading {
    position: absolute; left: 0; right: 0; top: 252px;
    text-align: center; color: var(--white);
    font-size: 27px; line-height: 37px; letter-spacing: 0.3px; text-transform: uppercase;
  }

  .story { top: 428px; width: 300px; height: 498px; padding: 16px 22px 0 30px;
    color: var(--white); font-size: 17.2px; line-height: 18.2px; }
  .story p + p { margin-top: 18px; }
  .story-founding { left: 0; background: linear-gradient(180deg, var(--blue-top), var(--blue-bottom)); }
  .story-approach { left: 300px; background: linear-gradient(180deg, var(--grey-top), var(--grey-bottom)); padding-left: 24px; }

  .summary { left: 600px; top: 0; width: 298px; height: 428px; background: var(--white); padding: 22px 20px 0 26px; }
  .panel-title { font-size: 29px; font-weight: 400; text-transform: uppercase; letter-spacing: 0.3px; line-height: 32px; }
  .summary .panel-title { color: #444; margin-bottom: 14px; }
  .summary p { font-size: 15.6px; line-height: 18px; }
  .summary-list { list-style: none; margin: 16px 0 14px; }
  .summary-list li { position: relative; padding-left: 22px; font-size: 15.6px; line-height: 17px; margin-bottom: 16px; }
  .summary-list li::before { content: ""; position: absolute; left: 2px; top: 6px; width: 7px; height: 7px; border-radius: 50%; background: var(--bullet); }
  .summary .spaced { line-height: 20px; margin-bottom: 19px; }

  .culture { left: 600px; top: 428px; width: 298px; height: 223px; background: var(--panel-light); padding: 20px 20px 0 26px; font-size: 13.8px; line-height: 17px; }
  .culture p + p { margin-top: 16px; }

  .bridge-photo { left: 600px; top: 651px; width: 298px; height: 275px;
    background: linear-gradient(180deg, var(--sky-top) 0%, #3f5a60 35%, var(--sky-mid) 62%, var(--sky-low) 100%); }
  .closing-heading { position: absolute; left: 26px; top: 22px; color: var(--white);
    font-size: 28px; line-height: 36.5px; text-transform: uppercase; }

  .services { left: 898px; top: 0; width: 302px; height: 855px;
    background: linear-gradient(180deg, var(--red), var(--red-deep)); color: var(--white); padding: 24px 10px 0 26px; }
  .services .panel-title { font-size: 27px; line-height: 27px; }
  .service-group { font-size: 22px; line-height: 22px; text-transform: uppercase; margin: 14px 0 14px; font-weight: 400; }
  .service-list { list-style: none; font-size: 15.6px; line-height: 16.7px; }
  .service-list li::before { content: "• "; }
  .service-list.gapped li { margin-bottom: 16px; }
  .service-list.gapped li.tight { margin-bottom: 0; }

  .signature { left: 898px; top: 855px; width: 302px; height: 71px; background: var(--white);
    display: flex; align-items: center; padding-left: 30px; gap: 12px; }
  .signature-dot { width: 42px; height: 42px; border-radius: 50%; background: var(--blue-bottom); }
  .signature-name { font-size: 20px; color: #333; letter-spacing: 0.5px; }
</style>
</head>
<body>
<div class="brochure">

  <section class="panel founders-photo" role="img" aria-label="Portrait photograph of the two company founders, father and son, in dark clothing against a textured dark grey backdrop">
    <h1 class="about-heading">— About Us —<br>We appreciate your time and the<br>opportunity to introduce<br>ourselves to you.</h1>
  </section>

  <section class="panel story story-founding">
    <p>Vell Tarnmoor was founded in 2007 by my father and I. We genuinely share a lifelong friendship established on mutual respect, wholehearted trust, and a compelling desire to make progress that benefits our surroundings.</p>
    <p>With over 60 years of diversely combined experience, my father with +45yrs. and myself with +15yrs., we have been blessed with countless opportunities to build genuine relationships with extremely talented individuals who commonly share similar moral beliefs and characteristics. We are grateful for their mutual trust in us and our teams’ keen interest in exceeding expectations of our clients. We have extreme confidence in our resources and we are proud for them to represent us.</p>
  </section>

  <section class="panel story story-approach">
    <p>Our diverse experience in various industries enables us to offer our clients a unique systematic approach to solving technical challenges. We urge clients to engage us in discussions as early as project conception to offer our knowledge and various potential solutions to explore best options to accomplish objectives as efficiently as possible. We offer insight to clients to express our mutual interest in favorable results.</p>
    <p>We have successfully contributed to managing and executing many industrial construction projects ranging from small to large magnitude (mega projects) from concept to completion. We are confident our services will positively impact your bottom-line and contribute to your success.</p>
  </section>

  <section class="panel summary">
    <h2 class="panel-title">Summary</h2>
    <p>Vell Tarnmoor is a highly dynamic Industrial Services organization that specializes in:</p>
    <ul class="summary-list">
      <li>Construction Project<br>Management</li>
      <li>Technical Services</li>
      <li>Consulting</li>
    </ul>
    <p class="spaced">We strive to build long-term genuine relationships based on trust and results!</p>
    <p class="spaced">We proactively seek opportunities to add value by effectively utilizing our knowledge, integrity, and quality attributes to ensure desired results.</p>
  </section>

  <section class="panel culture">
    <p>The foundation of our organization’s culture is high integrity, character, and respect. We empower individuals that demonstrate strong leadership skills with the belief that good leaders create more leaders and encourage a strong sense of trust in our organization.</p>
    <p>We look forward to discussing how our partnership will contribute to your success!</p>
  </section>

  <section class="panel bridge-photo" role="img" aria-label="Photograph of a long suspension bridge stretching into a misty teal sky over water">
    <h2 class="closing-heading">We look<br>forward to<br>speaking with<br>you soon!</h2>
  </section>

  <section class="panel services">
    <h2 class="panel-title">Services &amp;<br>Industries</h2>
    <h3 class="service-group">Oil &amp; Gas</h3>
    <ul class="service-list">
      <li>Upstream (Land &amp; Offshore, Subsea)</li>
      <li>Midstream (Terminals &amp; Plants)</li>
      <li>Downstream (Refineries &amp; LNG)</li>
      <li>Petrochemical</li>
    </ul>
    <h3 class="service-group">Power Generation</h3>
    <ul class="service-list">
      <li>Nuclear Power</li>
      <li>Fossil Fuels</li>
      <li>Renewable Energy</li>
    </ul>
    <h3 class="service-group">Construction<br>Project Management</h3>
    <ul class="service-list">
      <li>Complete EPC Oversight</li>
      <li>Owner / Client Representation</li>
      <li>Independent 3rd Party</li>
      <li>Inspection</li>
      <li>Coordination</li>
      <li>All Project Resources</li>
    </ul>
    <h3 class="service-group">Technical Services</h3>
    <ul class="service-list gapped">
      <li>Turnkey Commissioning /<br>Completions</li>
      <li>Instrumentation &amp; Electrical<br>Technicians</li>
      <li class="tight">E&amp;I Construction</li>
      <li class="tight">Automation Integration Specialists</li>
      <li class="tight">Analytical Specialists – Process<br>Analyzers</li>
    </ul>
    <h3 class="service-group">Consulting</h3>
    <ul class="service-list">
      <li>Project Management Consulting</li>
      <li>Project Optimization</li>
      <li>Project Controls</li>
      <li>Lean Practices</li>
      <li>Disaster Recovery</li>
      <li>Professional Development</li>
    </ul>
  </section>

  <footer class="panel signature">
    <span class="signature-dot"></span>
    <span class="signature-name">Vell Tarnmoor</span>
  </footer>

</div>
</body>
</html>
```